Business Card Design Project : Ferncliff Media

In preparation for market launch, Whistler's Ferncliff Media require the development of a business card. Ferncliff Media is a Community online publishing web portal. We provide the the city of Whistler located in B.C. (Canada) business directories, News, Classified ads, News, Events and blogs etc.

The main focus of the brand is to help local businesses to corporate with their online advertisement and marketing. Meeting our clients face to face is a must (B2B).

Target Market(s)

The target market is B2B customers. Business Owners to Marketing, advertising Managers

Industry/Entity Type

Business

Requirements
Must have
• - The business card will be two sided.
the BACK side will have our logo which consist of (icon, url,slogan) submited. The logo will be middle and centred.

The FRONT side should have company details:

Company Legal Name: TALLPINE FERNCLIFF MEDIA

Dale Morrow
Director of Sales & Marketing

www.tallpineferncliff.biz
dale@tallpineferncliff.biz

Phone: 604 555 0138
#2217 - 581 E. Harlow Ave.
Vancouver, B.C. V6N2K4 Canada
Nice to have
• - For the "FRONT" side of our business card. You can separate or re-arrange with our logo components (icon, logo,slogan). It does not have to be together.

Also our company legal name is rather long so arrange or organize the name in a way to make it shorter. Your experience and creativity will have to come in play.
Should not have
• should not have other colors beside logo color and black text (2 colors). Also nothing Three dimensional

```html
<!DOCTYPE html>
<html lang="en">
<head>
<meta charset="utf-8">
<title>Tallpine Ferncliff Media – Business Card</title>
<link rel="stylesheet" href="https://fonts.googleapis.com/css2?family=Arimo:wght@700&family=Audiowide&family=Lobster&family=Saira+Semi+Condensed:wght@700&family=Source+Sans+3:wght@400;700&display=swap">
<style>
  :root {
    --brand-blue: #0a7bcf;
    --ink: #111111;
    --paper: #ffffff;
    --backdrop: #e6e7e9;
  }
  * { box-sizing: border-box; margin: 0; padding: 0; }
  html, body {
    width: 940px;
    height: 1200px;
    overflow: hidden;
    background: var(--backdrop);
  }
  .canvas {
    position: relative;
    width: 940px;
    height: 1200px;
  }
  .card {
    position: absolute;
    left: 31px;
    width: 878px;
    height: 498px;
    background: var(--paper);
    overflow: hidden;
  }
  .card--front { top: 40px; }
  .card--back { top: 632px; }

  /* Front side */
  .wave-band {
    position: absolute;
    inset: 0;
    width: 878px;
    height: 498px;
  }
  .wave-band path { fill: var(--brand-blue); }
  .company-name {
    position: absolute;
    right: 29px;
    top: 44px;
    font-family: "Saira Semi Condensed", sans-serif;
    font-weight: 700;
    font-size: 36px;
    letter-spacing: 1px;
    color: var(--brand-blue);
    white-space: nowrap;
  }
  .person-name {
    position: absolute;
    left: 78px;
    top: 168px;
    font-family: "Lobster", cursive;
    font-size: 54px;
    line-height: 1;
    color: var(--ink);
  }
  .person-title {
    position: absolute;
    left: 78px;
    top: 246px;
    font-family: "Audiowide", sans-serif;
    font-size: 13.5px;
    letter-spacing: 2.4px;
    color: var(--ink);
    white-space: nowrap;
  }
  .online-contact {
    position: absolute;
    left: 78px;
    top: 371px;
    font-family: "Arimo", sans-serif;
    font-weight: 700;
    font-size: 18px;
    line-height: 24px;
    color: var(--brand-blue);
    list-style: none;
  }
  .postal-contact {
    position: absolute;
    right: 29px;
    top: 408px;
    font-family: "Arimo", sans-serif;
    font-weight: 700;
    font-size: 18px;
    line-height: 24px;
    color: var(--paper);
    text-align: right;
    font-style: normal;
  }

  /* Back side */
  .back-lockup {
    position: absolute;
    left: 0;
    right: 0;
    top: 252px;
    text-align: center;
  }
  .back-url {
    font-family: "Source Sans 3", sans-serif;
    font-weight: 700;
    font-size: 42px;
    line-height: 1;
    letter-spacing: -0.5px;
    color: var(--ink);
  }
  .back-slogan {
    margin-top: 6px;
    padding-left: 6px;
    font-family: "Source Sans 3", sans-serif;
    font-weight: 400;
    font-size: 30px;
    line-height: 1;
    letter-spacing: -0.5px;
    color: var(--brand-blue);
  }
</style>
</head>
<body>
<main class="canvas">

  <section class="card card--front" aria-label="Business card, front">
    <svg class="wave-band" viewBox="0 0 878 498" aria-hidden="true">
      <path d="M0,452 C250,440 420,410 540,350 C650,295 760,240 878,236 L878,498 L0,498 Z"/>
    </svg>

    <p class="company-name">TALLPINE FERNCLIFF MEDIA</p>

    <h1 class="person-name">Dale Morrow</h1>
    <p class="person-title">DIRECTOR OF SALES &amp; MARKETING</p>

    <ul class="online-contact">
      <li>www.tallpineferncliff.biz</li>
      <li>dale@tallpineferncliff.biz</li>
    </ul>

    <address class="postal-contact">
      Phone: 604 555 0138<br>
      #2217 - 581 E. Harlow Ave.<br>
      Vancouver, B.C. V6N2K4 Canada
    </address>
  </section>

  <section class="card card--back" aria-label="Business card, back">
    <div class="back-lockup">
      <p class="back-url">www.tallpineferncliff.biz</p>
      <p class="back-slogan">Your information gateway</p>
    </div>
  </section>

</main>
</body>
</html>
```